CLS Business card, letterhead, and stationery, email tag, fax cover
Clear and Professional material
Simple
Léandre Ormessac
Directeur des ventes
47, rue de Valmorin
Paris , 75016
France
leandre@clsys.fr
www.clsys.fr
Logo + tag line
LOGO
SMALL LOGO

```html
<!DOCTYPE html>
<html lang="fr">
<head>
<meta charset="utf-8">
<title>CLS – Cartes de visite</title>
<link href="https://fonts.googleapis.com/css2?family=Open+Sans:wght@400;600;700&display=swap" rel="stylesheet">
<style>
  :root {
    --backdrop: #1d1d1f;
    --card: #ffffff;
    --card-edge: #e9ebec;
    --accent: #3ea9cf;
    --ink: #4a4f55;
    --ink-soft: #8a9096;
    --figure-light: #dfe7ec;
    --figure-mid: #9fc9dc;
  }
  * { margin: 0; padding: 0; box-sizing: border-box; }
  html, body { width: 1200px; height: 945px; overflow: hidden; }
  body {
    background: var(--backdrop);
    font-family: "Open Sans", Arial, sans-serif;
    color: var(--ink);
    position: relative;
  }
  .card {
    position: absolute;
    width: 520px;
    height: 320px;
    background: linear-gradient(180deg, #ffffff 0%, #f4f6f7 100%);
    border: 1px solid var(--card-edge);
    border-radius: 22px;
    box-shadow: 0 12px 30px rgba(0,0,0,.55);
    overflow: hidden;
  }
  .card--front { left: 170px; top: 225px; }
  .card--back  { left: 500px; top: 580px; }

  .brand { position: absolute; display: flex; align-items: flex-end; gap: 10px; }
  .brand__figure {
    background: linear-gradient(160deg, var(--figure-mid), var(--figure-light));
    border-radius: 40% 40% 20% 20%;
  }
  .brand__text { display: flex; flex-direction: column; }
  .brand__name {
    font-weight: 600;
    color: var(--ink);
    line-height: 1.1;
  }
  .brand__tagline { color: var(--accent); font-weight: 400; }

  .card--front .brand { left: 22px; top: 26px; }
  .card--front .brand__figure { width: 62px; height: 110px; }
  .card--front .brand__name { font-size: 22px; }
  .card--front .brand__tagline { font-size: 12px; margin-top: 4px; }

  .decor {
    position: absolute; right: 20px; top: 40px;
    width: 140px; height: 150px;
    background: radial-gradient(ellipse at 50% 40%, #eceff1 0%, rgba(255,255,255,0) 70%);
  }

  .contact {
    position: absolute; left: 0; top: 168px;
    padding-left: 28px;
    border-left: 8px solid var(--accent);
    font-size: 11.5px; line-height: 16px;
    color: var(--ink);
  }
  .contact dt { display: inline; color: var(--accent); font-weight: 700; }
  .contact dd { display: inline; }
  .contact__row { display: block; }

  .person { position: absolute; right: 30px; top: 192px; text-align: right; }
  .person__name { font-size: 17px; font-weight: 600; color: var(--accent); }
  .person__role { font-size: 12px; color: var(--ink-soft); margin-top: 2px; }

  .card--back .brand { left: 50%; top: 50%; transform: translate(-50%, -50%); }
  .card--back .brand__figure { width: 58px; height: 104px; }
  .card--back .brand__name { font-size: 22px; }
  .card--back .brand__tagline { font-size: 12px; margin-top: 4px; }
</style>
</head>
<body>

<section class="card card--front" aria-label="Recto de la carte de visite">
  <div class="decor" role="img" aria-label="Silhouette décorative pâle"></div>
  <div class="brand">
    <div class="brand__figure" role="img" aria-label="Illustration d'une silhouette féminine"></div>
    <div class="brand__text">
      <span class="brand__name">Corvane Lumis<br>Systems</span>
      <span class="brand__tagline">solutions avancées de la peau</span>
    </div>
  </div>

  <dl class="contact">
    <span class="contact__row">47, rue de Valmorin</span>
    <span class="contact__row">Paris , 75016</span>
    <span class="contact__row">France</span>
    <span class="contact__row"><dt>P :</dt> <dd>01.42.18.07.36</dd></span>
    <span class="contact__row"><dt>C :</dt> <dd>06.51.74.20.93</dd></span>
    <span class="contact__row"><dt>F :</dt> <dd>01.42.18.07.37</dd></span>
    <span class="contact__row"><dt>E :</dt> <dd>leandre@clsys.fr</dd></span>
    <span class="contact__row"><dt>W :</dt> <dd>www.clsys.fr</dd></span>
  </dl>

  <div class="person">
    <p class="person__name">Léandre Ormessac</p>
    <p class="person__role">Directeur des ventes</p>
  </div>
</section>

<section class="card card--back" aria-label="Verso de la carte de visite">
  <div class="brand">
    <div class="brand__figure" role="img" aria-label="Illustration d'une silhouette féminine"></div>
    <div class="brand__text">
      <span class="brand__name">Corvane Lumis<br>Systems</span>
      <span class="brand__tagline">solutions avancées de la peau</span>
    </div>
  </div>
</section>

</body>
</html>
```